Cookie needs a website

We need a website for a cookie company based in Mexico City. Our company (called Panes Doradillos) has been baking and crating all sorts of cookies and cakes for more than 35 years.
We started off as a family business and till this date we are still functioning as one. We need the design of the web to be more on the baking side as we have many types of cookies cakes, pastries & muffins. Key elements, home style baking, use colours black, white and red. Tabs we need: front page, who are we, our brands and contact Preferable in Spanish. Im sure you have questions, please contact us. This is for homepage PSD design only no CSS,XHTML or full website build or coding involved as this is design competition.
Updates

Some more information has been added. Thanks is advance for your talent!

Target Market(s)

Target is general public, mostly families. Our product is not a luxury good,more like an affordable treat, however we do use very high quality products and high quality standards. Our motive is natural ingredients and home baked goods.
Our main point of sales is having shops inside department stores. Our own shops and selling to other businesses for re sale

Industry/Entity Type

Business

Font styles to use
Serif

Colors
ec2027
ffffff
333333

Requirements
Must have
• Baking oriented. An oven would be nice since we bake in front of our clients.
Colors we use also important
Nice to have
• make it home. (you have design freedom)
Below are the logos PD is the company name. Tomelo is one of our branches and the the pictures are from the cookies we make
Should not have
• PLEASE NO corny, over colorfull or tacky designs!!

```html
<!DOCTYPE html>
<html lang="en">
<head>
<meta charset="utf-8">
<title>Panes Doradillos</title>
<link href="https://fonts.googleapis.com/css2?family=Great+Vibes&family=Lato:ital,wght@0,400;0,700;1,400;1,700&display=swap" rel="stylesheet">
<style>
:root{
  --ink:#333333;
  --night:#1c1714;
  --coral:#fb6462;
  --red:#ec2027;
  --cream:#f2e9cf;
  --white:#ffffff;
  --muted:#6b6b6b;
  --line:#d9ceb0;
}
*{box-sizing:border-box;margin:0;padding:0}
html,body{width:938px;height:1200px;overflow:hidden}
body{font-family:'Lato',sans-serif;color:var(--ink);background:var(--cream)}
.canvas{position:relative;width:938px;height:1200px;overflow:hidden;background:var(--cream)}
.abs{position:absolute}
.script{font-family:'Great Vibes',cursive;font-weight:400}

/* header */
.site-header{left:0;top:0;width:938px;height:90px}
.hero-band{left:0;top:80px;width:938px;height:412px;background:var(--coral)}
.nav-link{top:22px;font-size:33px;color:var(--white);text-decoration:none;line-height:1;word-spacing:6px}
.brand-badge{left:410px;top:0;width:120px;height:112px}
.brand-mark{left:410px;top:28px;width:120px;text-align:center;font-size:40px;font-weight:700;color:var(--night);letter-spacing:1px}

/* slider */
.slide-photo{left:98px;top:125px;width:552px;height:292px;background:radial-gradient(circle at 40% 45%,#8a5a3a 0%,#5a3522 45%,#c9a27a 80%,#b08a66 100%)}
.slide-btn{top:391px;width:26px;height:26px}
.slide-btn.prev{left:596px;background:#2f2b2a}
.slide-btn.next{left:623px;background:var(--red)}

.recipes{left:650px;top:125px;width:190px;height:292px;background:var(--white)}
.recipes h2{position:absolute;left:9px;top:15px;font-size:18px;font-style:italic;font-weight:400;color:var(--ink)}
.recipes .rule{position:absolute;left:9px;width:171px;height:1px;background:var(--ink)}
.recipe{position:absolute;left:9px;width:175px;height:74px}
.recipe .thumb{position:absolute;left:0;top:0;width:74px;height:74px}
.recipe h3{position:absolute;left:81px;top:-2px;font-size:14px;font-weight:400;color:var(--night)}
.recipe p{position:absolute;left:81px;top:20px;width:92px;font-size:10.5px;line-height:13px;color:var(--muted)}
.recipe .details{position:absolute;left:82px;top:61px;font-size:12px;font-style:italic;color:var(--night)}
.view-more{left:659px;top:373px;width:56px;height:23px;background:var(--red);color:var(--white);font-size:10.5px;font-style:italic;line-height:23px;text-align:center}

/* categories */
.category-tab{top:511px;width:64px;height:64px;border-radius:50%;background:var(--ink)}
.category-tab.dark{background:var(--night)}
.category{top:437px;width:235px;height:113px}
.category .photo{position:absolute;left:0;top:0;width:118px;height:113px}
.category .panel{position:absolute;left:118px;top:0;width:117px;height:113px;background:var(--ink)}
.category h3{position:absolute;left:118px;top:4px;width:117px;text-align:center;font-size:32px;color:var(--white)}
.category p{position:absolute;left:133px;top:44px;width:100px;font-size:13px;line-height:19px;color:var(--white)}
.category-more{top:539px;width:118px;text-align:center;font-size:13px;color:var(--white)}

/* intro */
.tagline{left:0;top:598px;width:938px;text-align:center;font-size:40px;color:var(--night);line-height:1.1}
.tagline em{font-style:normal;color:var(--coral)}
.intro{left:144px;top:661px;width:650px;text-align:center;font-size:11px;line-height:19px;color:var(--ink)}
.divider{left:115px;top:733px;width:688px;height:1px;background:var(--line)}

/* feature cards */
.feature{top:768px;width:235px;height:302px;background:var(--white);box-shadow:0 2px 3px rgba(0,0,0,.35)}
.feature .photo{position:absolute;left:0;top:0;width:235px;height:149px}
.feature h3{position:absolute;left:0;top:158px;width:235px;text-align:center;font-size:16.5px;font-style:italic;font-weight:400;line-height:19px;color:var(--night)}
.feature p{position:absolute;left:16px;top:206px;width:203px;text-align:center;font-size:9.5px;line-height:13.5px;color:var(--ink)}
.feature .read{position:absolute;left:77px;top:266px;width:72px;height:27px;background:var(--night);color:var(--white);font-size:12px;font-style:italic;line-height:27px;text-align:center}

/* footer */
.site-footer{left:0;top:1108px;width:938px;height:92px;background:var(--night);color:var(--white)}
.footer-nav{position:absolute;left:97px;top:16px;font-size:12px;word-spacing:1px}
.footer-nav span{margin:0 8px}
.copyright{position:absolute;left:96px;top:57px;font-size:12px}
.social{position:absolute;right:94px;top:54px;display:flex;align-items:center;gap:9px;font-size:12px}
.social .net{display:flex;align-items:center;gap:4px;font-size:10px}
.social .dot{width:12px;height:12px;border-radius:50%;background:var(--white)}
</style>
</head>
<body>
<div class="canvas">

  <div class="abs hero-band"></div>

  <svg class="abs site-header" viewBox="0 0 938 90" aria-hidden="true">
    <defs>
      <pattern id="zigzag" x="0" y="82" width="8" height="4" patternUnits="userSpaceOnUse">
        <path d="M0 0 L4 4 L8 0Z" fill="#333333"/>
      </pattern>
    </defs>
    <rect x="0" y="0" width="938" height="82" fill="#333333"/>
    <rect x="0" y="82" width="938" height="4" fill="url(#zigzag)"/>
  </svg>

  <a class="abs nav-link script" style="left:120px">Home</a>
  <a class="abs nav-link script" style="left:236px">About Us</a>
  <a class="abs nav-link script" style="left:587px">Products</a>
  <a class="abs nav-link script" style="left:717px">Contact Us</a>

  <svg class="abs brand-badge" viewBox="0 0 120 112" aria-hidden="true">
    <path d="M0 0H120V96 Q120 100 114 101 L60 112 L6 101 Q0 100 0 96Z" fill="#ffffff"/>
  </svg>
  <div class="abs brand-mark">PD</div>

  <div class="abs slide-photo" role="img" aria-label="Photo of chocolate tartlets dusted with cocoa and topped with chocolate curls"></div>
  <div class="abs slide-btn prev"><svg width="26" height="26" viewBox="0 0 26 26"><path d="M15 7 9 13 15 19" stroke="#fff" stroke-width="3" fill="none"/></svg></div>
  <div class="abs slide-btn next"><svg width="26" height="26" viewBox="0 0 26 26"><path d="M11 7 17 13 11 19" stroke="#fff" stroke-width="3" fill="none"/></svg></div>

  <aside class="abs recipes">
    <h2>Fresh Recipes</h2>
    <div class="rule" style="top:45px"></div>
    <div class="recipe" style="top:59px">
      <div class="thumb" role="img" aria-label="Photo of a slice of chocolate cake" style="background:linear-gradient(135deg,#d8d4cf,#3a2419 55%,#efeae4)"></div>
      <h3>Cakes</h3>
      <p>Lorem ipsum dolor sit amet, consect-etur...</p>
      <span class="details">Details »</span>
    </div>
    <div class="recipe" style="top:160px">
      <div class="thumb" role="img" aria-label="Photo of chocolate chip cookies" style="background:linear-gradient(135deg,#e4ddd6,#6e4632 50%,#4a2e20)"></div>
      <h3>Cookies</h3>
      <p>Lorem ipsum dolor sit amet, consect-etur...</p>
      <span class="details">Details »</span>
    </div>
    <div class="rule" style="top:244px"></div>
  </aside>
  <div class="abs view-more">View More</div>

  <div class="abs category-tab" style="left:244px"></div>
  <div class="abs category-tab dark" style="left:499px"></div>
  <div class="abs category-tab" style="left:753px"></div>

  <div class="abs category" style="left:98px">
    <div class="photo" role="img" aria-label="Photo of sliced chocolate loaf cake" style="background:linear-gradient(135deg,#5a3324,#2c1810 60%,#e8e2dc)"></div>
    <div class="panel"></div>
    <h3 class="script">Cake</h3>
    <p>nulidas vacsques asey yoleacene</p>
  </div>
  <div class="abs category" style="left:352px">
    <div class="photo" role="img" aria-label="Photo of swirl cookies with star anise" style="background:linear-gradient(135deg,#c98a4a,#7a4a26 55%,#5a3420)"></div>
    <div class="panel"></div>
    <h3 class="script">Cookies</h3>
    <p>nulidas vacsques asey yoleacene</p>
  </div>
  <div class="abs category" style="left:606px">
    <div class="photo" role="img" aria-label="Photo of chocolate muffins with white icing" style="background:linear-gradient(135deg,#b8342a,#3a2018 55%,#2a160f)"></div>
    <div class="panel"></div>
    <h3 class="script">Muffins</h3>
    <p>nulidas vacsques asey yoleacene</p>
  </div>
  <div class="abs category-more" style="left:216px">More</div>
  <div class="abs category-more" style="left:472px">More</div>
  <div class="abs category-more" style="left:726px">More</div>

  <h1 class="abs tagline script">Make Your <em>Life Tasty!</em></h1>
  <p class="abs intro">Beciegast kiausnveriti vitaesaert asety kertya aset aplica bosafae keuestyasne moseade keryiuasa doloertymuas faserani ptaiades kertyaser daesraeds. Casrolern atur aut oditaut. onsequuntur magni dolqui ratione voluptatemsequi nesrentro quiserstqui dosum, quia dolor asasaert nsectetur adipivelisuia non numquam eius modi teincidunt, ut labore et dolore magnam.</p>
  <div class="abs divider"></div>

  <article class="abs feature" style="left:98px">
    <div class="photo" role="img" aria-label="Photo of a pink frosted cupcake with a chocolate roll" style="background:linear-gradient(135deg,#e8e4e0,#e86a76 55%,#5a2e1e)"></div>
    <h3>Decorating<br>&amp; Baking Cupcakes</h3>
    <p>Vaserbo nerafaes sety krscakertsvitae ertyas-nemo lasec vasptaia goertayse. maloreo qui ratione voluptate kjahsaus msequi nesciunt, nequisquam estasas.</p>
    <div class="read">Read More</div>
  </article>
  <article class="abs feature" style="left:352px">
    <div class="photo" role="img" aria-label="Photo of glazed roast lamb on rice with mint" style="background:linear-gradient(135deg,#e6dcc6,#6a3a1c 50%,#d8cfb8)"></div>
    <h3>Roast Lamb<br>With Mint Sauce</h3>
    <p>Vaserbo nerafaes sety krscakertsvitae ertyas-nemo lasec vasptaia goertayse. maloreo qui ratione voluptate kjahsaus msequi nesciunt, nequisquam estasas.</p>
    <div class="read">Read More</div>
  </article>
  <article class="abs feature" style="left:606px">
    <div class="photo" role="img" aria-label="Photo of chocolate nut cookies" style="background:linear-gradient(135deg,#6a4634,#4a2e22 50%,#8a6450)"></div>
    <h3>Nuts<br>Cookies</h3>
    <p>Vaserbo nerafaes sety krscakertsvitae ertyas-nemo lasec vasptaia goertayse. maloreo qui ratione voluptate kjahsaus msequi nesciunt, nequisquam estasas.</p>
    <div class="read">Read More</div>
  </article>

  <footer class="abs site-footer">
    <nav class="footer-nav">Home<span>|</span>About Us<span>|</span>Products<span>|</span>Brands<span>|</span>Contact Us</nav>
    <div class="copyright">Copyright By Panes Doradillos</div>
    <div class="social">Follow Us :
      <span class="net"><span class="dot"></span>Vecino</span>
      <span class="net"><span class="dot"></span>Trino</span>
      <span class="net"><span class="dot"></span>Gremio</span>
      <span class="net"><span class="dot"></span>Plaza</span>
    </div>
  </footer>

</div>
</body>
</html>
```